Christian Camp Meetings Website Design

**Do not contact me privately; all inquiries will be ignored.**

Industry: Nonprofit Christian camp meetings for children, youth, and adults.

Target Market: Families and individuals seeking a faith-based camp experience.

Description:
This website should provide a visually appealing and easy-to-navigate platform that clearly highlights how visitors can register for camp events and make donations. A straightforward design will make it simple for users to access registration forms, donation buttons, and key event & camp details.

Look and Feel:
• Clean, user-friendly layout focused on clarity and accessibility.
• Primarily blue tones to evoke a calm and welcoming atmosphere.
• Clear, readable Google fonts only.
• If using images only use royalty-free stock photos showcasing participants at camp activities, encouraging new registrations and donations.

Pages to Create:
1. Main Page: A welcoming overview that prominently features call-to-action buttons for registration and donations.
2. Christian Camp Meetings Page: Detailed event information with links to registration forms and suggested donation amounts.
3. Youth Program Page: Descriptions of youth events, programs, and an easy-to-find registration link.
4. Children’s Camp Page: Information about the children’s Bible camp, with a focus on how parents can register their kids.
5. History Page: A brief look at the organization’s origins, with an integrated “Donate Now” button to support ongoing programs.

Examples of Desired Style:
• https://www.brightharborfolk.org/nwr/
• https://walkingtruepath.com/
• https://www.pinevalechapel.org/
• https://kw.church/

Content Source:
Use content from the link provided in the attachment here as the primary source for all textual and media content.

Important Notes:
• Do not contact me privately; all inquiries will be ignored.
• The website should emphasize registration and donations as key actions.
• Avoid overlapping elements in the design; maintain a clean and structured layout.
• Ensure that only Google fonts and royalty-free stock photos are used.

Target Market(s)

Christian families looking for events

Industry/Entity Type

Christian faith based camp

Number of Pages Required

5+ page

Colors
0094D4
00A9DD
6FCCEA
C7EBF8
E9F6FB

Requirements
Should not have
• No search bar, limited or no overlapping elements

```html
<!DOCTYPE html>
<html lang="en">
<head>
<meta charset="utf-8">
<title>Youth Programs – Cedar Ridge Holiness Camp Association</title>
<link href="https://fonts.googleapis.com/css2?family=Noto+Serif:wght@400&family=Poppins:wght@400;500;600;700&display=swap" rel="stylesheet">
<style>
:root{
  --blue:#0094D4;
  --blue-deep:#007fba;
  --blue-light:#00A9DD;
  --heading-blue:#1d90cf;
  --green:#8ab86e;
  --dark:#272b30;
  --input:#3a3f45;
  --ink:#222;
  --white:#fff;
}
*{margin:0;padding:0;box-sizing:border-box}
html,body{width:853px;height:1200px;overflow:hidden}
body{position:relative;background:var(--white);font-family:"Poppins",sans-serif;color:var(--ink)}
.serif{font-family:"Noto Serif",serif;font-weight:400}
.abs{position:absolute}

/* header */
.brand{left:149px;top:27px;width:140px;height:24px;display:flex;align-items:center;gap:7px;font-family:"Poppins",sans-serif;font-weight:600;font-size:10px;color:var(--ink);white-space:nowrap}
.brand-dot{width:18px;height:18px;border-radius:50%;background:var(--blue);flex:none}
.btn{display:flex;align-items:center;justify-content:center;gap:7px;color:var(--white);font-weight:600;border-radius:4px;text-decoration:none}
.btn svg{flex:none}
.btn-green{background:var(--green)}
.btn-blue{background:var(--blue)}
.hdr-donate{left:519px;top:23px;width:92px;height:31px;font-size:8.5px}
.hdr-register{left:616px;top:23px;width:88px;height:31px;font-size:8.5px}

/* nav */
.nav{left:0;top:77px;width:853px;height:40px;background:var(--blue)}
.nav a{position:absolute;top:0;height:40px;line-height:40px;color:var(--white);font-size:8.3px;font-weight:500;text-decoration:none;text-align:center}
.nav .active{background:var(--blue-deep)}
.nav .contact{background:var(--green);line-height:42px}

/* hero */
.hero{left:0;top:117px;width:853px;height:290px;
  background:
    linear-gradient(180deg,rgba(255,255,255,0) 55%,rgba(255,255,255,.75) 80%,#fff 100%),
    radial-gradient(ellipse at 30% 15%,#8c9ba0 0%,rgba(140,155,160,0) 35%),
    linear-gradient(90deg,#4f5e4a 0%,#3f4d55 30%,#3a4658 55%,#4b5a49 80%,#56633f 100%)}
.hero-title{left:0;top:146px;width:853px;text-align:center;font-size:32px;color:var(--white)}
.hero-text{left:166px;top:204px;width:521px;text-align:center;font-size:10.9px;line-height:16px;color:var(--white)}

/* meetings */
.section-title{left:0;top:374px;width:853px;text-align:center;font-size:23px;color:var(--heading-blue)}
.card-img{top:431px;width:177px;height:113px}
.card-title{top:556px;width:177px;text-align:center;font-size:14px;color:var(--heading-blue)}
.card-meta{top:580px;width:177px;text-align:center;font-size:7.3px;line-height:11px;color:#333}
.card-btn{top:619px;width:75px;height:25px;font-size:6.5px;font-weight:400}

/* giving band */
.giving{left:0;top:684px;width:853px;height:283px;
  background:linear-gradient(180deg,#d9c7a4 0%,#6aa6cf 12%,#1a8fd0 32%,#00a0dc 50%,var(--blue) 75%)}
.giving-title{left:0;top:732px;width:853px;text-align:center;font-size:22px;line-height:25px;color:var(--white)}
.giving-text{left:0;top:802px;width:853px;text-align:center;font-size:11px;line-height:16px;color:var(--white)}
.giving-btn{left:355px;top:857px;width:143px;height:45px;font-size:11px;gap:10px}

/* footer */
.footer{left:0;top:967px;width:853px;height:233px;background:var(--dark)}
.seal{left:378px;top:919px;width:96px;height:96px;border-radius:50%;background:var(--white);display:flex;align-items:center;justify-content:center;font-family:"Poppins",sans-serif;font-weight:600;color:var(--ink);font-size:9px;line-height:12px;text-align:center;padding:0 14px}
.f-head{font-size:14px;color:var(--white)}
.f-text{font-size:7.3px;line-height:10.7px;color:var(--white)}
.mail{left:340px;top:1084px;width:173px;height:36px;background:var(--input);color:var(--white);font-size:7.3px;display:flex;align-items:center;justify-content:space-between;padding:0 13px}
.social{top:1135px;width:10px;height:10px;border:1.3px solid var(--white);border-radius:50%}
.f-register{left:560px;top:1041px;width:143px;height:45px;font-size:11px;gap:12px}
.f-donate{left:562px;top:1091px;width:142px;height:45px;font-size:11px;gap:12px}
.copy{left:0;top:1173px;width:853px;text-align:center;font-size:8.3px;color:var(--white)}
</style>
</head>
<body>

<header>
  <div class="abs brand"><span class="brand-dot"></span>Cedar Ridge Camp</div>
  <a class="abs btn btn-green hdr-donate" href="#">
    <svg width="15" height="12" viewBox="0 0 15 12" fill="none" stroke="#fff" stroke-width="1"><path d="M1 7h3v4H1zM4 8c2 0 3-1 5-1s2 1 0 1.5M4 10.5c3 .5 5 0 9-3"/><path d="M10 5.5 7.5 3a1.4 1.4 0 0 1 2.5-1.5A1.4 1.4 0 0 1 12.5 3z"/></svg>
    Donate</a>
  <a class="abs btn btn-blue hdr-register" href="#">
    <svg width="13" height="13" viewBox="0 0 13 13" fill="none" stroke="#fff" stroke-width="1.1"><circle cx="6.5" cy="4" r="3"/><path d="M1 12.5c.5-3 2.5-4.5 5.5-4.5s5 1.5 5.5 4.5"/></svg>
    Register</a>
</header>

<nav class="abs nav">
  <a href="#" style="left:150px;width:45px">Home</a>
  <a href="#" style="left:215px;width:80px">Camp Meetings</a>
  <a href="#" class="active" style="left:313px;width:89px">Youth Programs</a>
  <a href="#" style="left:420px;width:86px">Children’s Camp</a>
  <a href="#" style="left:528px;width:44px">History</a>
  <a href="#" class="contact" style="left:607px;width:97px">Contact us</a>
</nav>

<section>
  <div class="abs hero" role="img" aria-label="Young people raising their hands outdoors above a green valley at sunrise"></div>
  <h1 class="abs serif hero-title">Youth Programs</h1>
  <p class="abs hero-text">Cedar Ridge Camp’s Youth Program is designed to inspire and equip young people with a strong foundation in faith while providing an unforgettable camp experience. Through engaging activities, worship, and fellowship, youth will grow spiritually and build lifelong friendships.</p>
</section>

<section>
  <h2 class="abs serif section-title">Upcoming Camp Meetings</h2>

  <div class="abs card-img" style="left:149px;background:linear-gradient(120deg,#3a302a,#8a7a6a 55%,#c9bfb3)" role="img" aria-label="Young people clapping while a guitarist plays"></div>
  <h3 class="abs serif card-title" style="left:149px">Spring Revival Meeting</h3>
  <p class="abs card-meta" style="left:149px">March 15-17, 2025<br>Guest Speaker: Pastor Dalen</p>
  <a class="abs btn btn-blue card-btn" style="left:200px" href="#">Register Now</a>

  <div class="abs card-img" style="left:338px;background:linear-gradient(180deg,#1d2a78,#4b5fb8 40%,#3a3250 75%,#2a221e)" role="img" aria-label="Worship service with raised hands facing a lit stage"></div>
  <h3 class="abs serif card-title" style="left:338px">Summer Camp Meeting</h3>
  <p class="abs card-meta" style="left:338px">June 10-15, 2025<br>Worship &amp; Bible Study Sessions</p>
  <a class="abs btn btn-blue card-btn" style="left:389px" href="#">Register Now</a>

  <div class="abs card-img" style="left:526px;background:linear-gradient(180deg,#8f8068,#b9ad97 40%,#4a4450 75%,#2b2a33)" role="img" aria-label="Worship band on stage with congregation in front"></div>
  <h3 class="abs serif card-title" style="left:526px">Youth Renewal Weekend</h3>
  <p class="abs card-meta" style="left:526px">July 5-7, 2025<br>Special Program for Teens</p>
  <a class="abs btn btn-blue card-btn" style="left:577px" href="#">Register Now</a>
</section>

<section>
  <div class="abs giving" role="img" aria-label="Blue sky background with soft sparkling light"></div>
  <h2 class="abs serif giving-title">Cedar Ridge Holiness Camp Association now<br>has online giving.</h2>
  <p class="abs giving-text">You can sign up for a one-time, weekly, or monthly gift.&nbsp; It is easy to edit<br>the amount or frequency or even cancel if you need to do that.</p>
  <a class="abs btn btn-green giving-btn" href="#">
    <svg width="21" height="17" viewBox="0 0 15 12" fill="none" stroke="#fff" stroke-width=".9"><path d="M1 7h3v4H1zM4 8c2 0 3-1 5-1s2 1 0 1.5M4 10.5c3 .5 5 0 9-3"/><path d="M10 5.5 7.5 3a1.4 1.4 0 0 1 2.5-1.5A1.4 1.4 0 0 1 12.5 3z"/></svg>
    Donate Now</a>
</section>

<footer>
  <div class="abs footer"></div>
  <div class="abs seal">Cedar Ridge Camp</div>

  <h3 class="abs serif f-head" style="left:149px;top:1037px">Contact</h3>
  <p class="abs f-text" style="left:150px;top:1063px">Cedar Ridge Holiness Camp<br>412 Meadowlark Lane<br>Brookfield, IL 60513<br>Phone: 555-310-4726 (during camp)<br>Phone: 555-310-8842 (off season)</p>

  <h3 class="abs serif f-head" style="left:340px;top:1037px;width:173px;text-align:center">Stay Updated</h3>
  <p class="abs f-text" style="left:340px;top:1060px;width:173px;text-align:center">Join Our Mailing List</p>
  <div class="abs mail"><span>Enter your mail id</span>
    <svg width="8" height="8" viewBox="0 0 8 8" fill="none" stroke="#fff" stroke-width="1"><path d="M1 4h6M4.5 1.5 7 4 4.5 6.5"/></svg></div>
  <span class="abs social" style="left:399px" aria-label="Social profile"></span>
  <span class="abs social" style="left:420px" aria-label="Social profile"></span>
  <span class="abs social" style="left:441px" aria-label="Social profile"></span>

  <a class="abs btn btn-blue f-register" href="#">
    <svg width="18" height="18" viewBox="0 0 13 13" fill="none" stroke="#fff" stroke-width=".9"><circle cx="6.5" cy="4" r="3"/><path d="M1 12.5c.5-3 2.5-4.5 5.5-4.5s5 1.5 5.5 4.5"/></svg>
    Register Now</a>
  <a class="abs btn btn-green f-donate" href="#">
    <svg width="21" height="17" viewBox="0 0 15 12" fill="none" stroke="#fff" stroke-width=".9"><path d="M1 7h3v4H1zM4 8c2 0 3-1 5-1s2 1 0 1.5M4 10.5c3 .5 5 0 9-3"/><path d="M10 5.5 7.5 3a1.4 1.4 0 0 1 2.5-1.5A1.4 1.4 0 0 1 12.5 3z"/></svg>
    Donate Now</a>

  <p class="abs copy">© 2025 Cedar Ridge Holiness Camp. All Rights Reserved.</p>
</footer>

</body>
</html>
```